PTA Meeting Poster

We are looking to create a poster to invite parents of our school to our monthly PTA Meeting.

The copy should include:

PTA Meeting
This Wednesday
8:40am
in the Multi Purpose Room

All Welcome!

```html
<!DOCTYPE html>
<html lang="en">
<head>
<meta charset="utf-8">
<title>PTA Meeting</title>
<link rel="stylesheet" href="https://fonts.googleapis.com/css2?family=Alfa+Slab+One&family=Great+Vibes&display=swap">
<style>
  :root {
    --paper: #FFFF99;
    --frame-line: #C8C8FF;
    --ornament-tone: #EEEAA6;
    --title-box: #FFCC00;
    --title-shadow: #FFFF00;
    --title-ink: #7B2ACB;
    --meeting-ink: #6633FF;
    --banner: #FFFF00;
    --detail-ink: #006600;
    --welcome-ink: #FF0000;
  }
  html, body {
    margin: 0;
    padding: 0;
    overflow: hidden;
    background: var(--paper);
  }
  .poster {
    display: block;
    width: 899px;
    height: 1200px;
  }
  .poster-bg { fill: var(--paper); }
  .frame-line { fill: none; stroke: var(--frame-line); stroke-width: 2; }
  .corner-ornament { fill: var(--ornament-tone); }
  .title-shadow { fill: var(--title-shadow); }
  .title-box { fill: var(--title-box); }
  .title-text {
    font-family: "Alfa Slab One", Georgia, serif;
    font-size: 262px;
    fill: var(--title-ink);
  }
  .meeting-text {
    font-family: "Alfa Slab One", Georgia, serif;
    font-size: 136px;
    fill: var(--meeting-ink);
  }
  .banner { fill: var(--banner); }
  .detail-text {
    font-family: "Alfa Slab One", Georgia, serif;
    font-size: 86px;
    fill: var(--detail-ink);
    text-anchor: middle;
  }
  .welcome-text {
    font-family: "Great Vibes", "Brush Script MT", cursive;
    font-size: 84px;
    fill: var(--welcome-ink);
  }
</style>
</head>
<body>
<svg class="poster" viewBox="0 0 948 1265" width="899" height="1200" xmlns="http://www.w3.org/2000/svg">
  <rect class="poster-bg" x="0" y="0" width="948" height="1265"/>

  <rect class="frame-line" x="80" y="80" width="787" height="1103"/>

  <rect class="corner-ornament" role="img" aria-label="Floral vine corner ornament" x="62" y="60" width="170" height="165"/>
  <rect class="corner-ornament" role="img" aria-label="Floral vine corner ornament" x="715" y="60" width="172" height="165"/>
  <rect class="corner-ornament" role="img" aria-label="Floral vine corner ornament" x="62" y="1035" width="170" height="170"/>
  <rect class="corner-ornament" role="img" aria-label="Floral vine corner ornament" x="715" y="1035" width="172" height="170"/>

  <g class="title-block">
    <rect class="title-shadow" x="203" y="162" width="567" height="225"/>
    <rect class="title-box" x="189" y="150" width="567" height="225"/>
    <text class="title-text" x="218" y="361" textLength="522" lengthAdjust="spacingAndGlyphs">PTA</text>
  </g>

  <text class="meeting-text" x="166" y="496" textLength="612" lengthAdjust="spacingAndGlyphs">Meeting</text>

  <polygon class="banner" points="175,540 778,578 770,650 775,737 570,745 780,770 770,860 772,940 600,955 768,978 715,992 762,1018 630,1032 762,1068 157,1028 165,948 160,865 340,858 167,823 178,730 173,665 340,658 165,630 295,600 175,574 205,556"/>

  <g class="meeting-details">
    <text class="detail-text" x="476" y="628">This</text>
    <text class="detail-text" x="476" y="710" textLength="437" lengthAdjust="spacingAndGlyphs">Wednesday</text>
    <text class="detail-text" x="476" y="790">8.40 am</text>
    <text class="detail-text" x="476" y="872">in the</text>
    <text class="detail-text" x="476" y="955" textLength="522" lengthAdjust="spacingAndGlyphs">Multipurpose</text>
    <text class="detail-text" x="476" y="1036">Room</text>
  </g>

  <text class="welcome-text" x="250" y="1192" textLength="465" lengthAdjust="spacingAndGlyphs">All Welcome!</text>
</svg>
</body>
</html>
```